Modernise existing business card and letterhead designs

Based on the existing business card and letterhead design (in InDesign and Word formats respectively), I seek a new stationery design suite that has the following qualities:
For Business Cards:
* three colours only - blue (C=64, M=9, Y=0, K=0), grey and white
* two sided
* minimalist yet modern look
* retention of all text in AccordAlternate font
* retention of logo
* retention of QR code
* all else can be changed, including all the above in terms of size, location, and replacement of capital letter headers (eg address, telephone, fax, mobile, etc) with symbols
For Letterhead:
* single sided
* retention of logo
All files are available via https://www.filecrate.example/sh/k4pazr2mw9xq7tb/BBQxZr7pLmNvKeWtYuHsGfD3c?dl=0
The final output needs to be made available with the following requirements for download:
* business card template in at least Adobe InDesign CS3 version 5.0 format
* letterhead template in Word format, with associated files in EPS and JPEG embedded
* associated files in EPS and JPEG
* files of the fonts used
Target Market(s)
- Young entrepreneurs and business owners
- legislators and government bureaucrats
Industry/Entity Type
Leadership
Requirements
Must have
- - Use of logo, corporate font and corporate colour (C=64, M=9, Y=0, K=0)
- - as minimalistic as possible
- - modern look
- - retention of the (85 mm x 55 mm) dimensions of the business card design
- - retention of the A4 dimensions of the letterhead design
Nice to have
- - use of symbols instead of text wherever possible (eg capital letter titles for address, telephone, fax, mobile, e-mail, website, etc)
Should not have
- - avoid being too traditional

```html
<!DOCTYPE html>
<html lang="en">
<head>
<meta charset="utf-8">
<title>Letterhead – Harbourline Early Years Network</title>
<link rel="stylesheet" href="https://fonts.googleapis.com/css2?family=Exo+2:wght@400;500;600&display=swap">
<style>
  :root {
    --brand-blue: #3db8e8;
    --brand-grey: #55585b;
    --ink: #111111;
    --paper: #ffffff;
  }
  * { margin: 0; padding: 0; box-sizing: border-box; }
  html, body { width: 927px; height: 1200px; overflow: hidden; background: var(--paper); }
  .letterhead {
    position: relative;
    width: 927px;
    height: 1200px;
    background: var(--paper);
    font-family: "Exo 2", sans-serif;
    color: var(--ink);
  }
  .brand {
    position: absolute;
    left: 72px;
    top: 90px;
    display: flex;
    align-items: center;
    gap: 12px;
  }
  .brand-mark {
    width: 22px;
    height: 22px;
    background: var(--brand-blue);
  }
  .brand-name {
    font-size: 22px;
    font-weight: 500;
    color: var(--brand-grey);
    letter-spacing: -0.2px;
  }
  .recipient {
    position: absolute;
    left: 684px;
    top: 86px;
    font-size: 15px;
    line-height: 17.2px;
    font-style: normal;
    color: var(--ink);
    letter-spacing: 0.3px;
  }
  .recipient .date { margin-bottom: 34px; }
  .body-copy {
    font-family: Arial, Helvetica, sans-serif;
    font-size: 13.5px;
    color: var(--ink);
    position: absolute;
    left: 88px;
  }
  .salutation { top: 276px; }
  .closing { top: 880px; }
  .signatory { top: 938px; line-height: 14.5px; }
  .footer-band {
    position: absolute;
    background: linear-gradient(180deg, var(--brand-grey) 0%, var(--brand-grey) 45%, var(--brand-blue) 70%, var(--brand-blue) 100%);
  }
  .footer-band.main { left: 18px; top: 1072px; width: 382px; height: 110px; }
  .footer-band.side { left: 834px; top: 1072px; width: 76px; height: 84px; }
  .footer-details {
    position: absolute;
    left: 416px;
    top: 1088px;
    font-size: 12.5px;
    color: var(--brand-grey);
    line-height: 20.5px;
    letter-spacing: 0.4px;
  }
  .footer-details .org {
    font-size: 15px;
    font-weight: 600;
    color: var(--brand-blue);
    letter-spacing: 0.2px;
    margin-bottom: 1px;
  }
  .footer-details .label {
    color: var(--brand-blue);
    font-weight: 600;
    margin-right: 7px;
  }
  .contact-row { display: flex; }
  .contact-row .email { width: 236px; }
  .contact-row .phone { width: 132px; }
</style>
</head>
<body>
<main class="letterhead">
  <header class="brand">
    <span class="brand-mark"></span>
    <span class="brand-name">Harbourline Early Years Network</span>
  </header>

  <address class="recipient">
    <div class="date">date</div>
    <div>name</div>
    <div>title</div>
    <div>organization</div>
    <div>address1</div>
    <div>address2</div>
  </address>

  <p class="body-copy salutation">Dear &lt;name&gt;,</p>
  <p class="body-copy closing">Yours sincerely,</p>
  <p class="body-copy signatory">&lt;name&gt;<br>&lt;title&gt;</p>

  <div class="footer-band main" role="img" aria-label="Decorative band pattern in grey and blue"></div>
  <div class="footer-band side" role="img" aria-label="Small decorative pattern in grey and blue"></div>

  <footer class="footer-details">
    <div class="org">Harbourline Early Years Network</div>
    <div><span class="label">ABN</span>48 913 265 071</div>
    <div><span class="label">A</span>PO Box 418, Riverton&nbsp; NSW&nbsp; 2190</div>
    <div class="contact-row">
      <span class="email"><span class="label">E</span>office@harbourline.example</span>
      <span class="phone"><span class="label">P</span>1300 482 615</span>
      <span class="fax"><span class="label">F</span>1300 482 617</span>
    </div>
  </footer>
</main>
</body>
</html>
```